Business Card - Cooperate

Business Card for Larkfield Management Consulting

Target Market(s)

Corparte - b2B

Industry/Entity Type

Management Consulting - Professional Services

Contact Information for Business Card

Company Name , Slogan , Dummy Address,

Requirements
Must have
• Lead with lasting clarity

```html
<!DOCTYPE html>
<html lang="en">
<head>
<meta charset="utf-8">
<title>Larkfield Management Consulting – Business Card</title>
<link rel="stylesheet" href="https://fonts.googleapis.com/css2?family=Source+Sans+3:wght@400;600;700&display=swap">
<style>
  :root {
    --backdrop: #dedfe1;
    --navy: #1b1c45;
    --navy-deep: #14163a;
    --brand-blue: #2c55b8;
    --teal: #1f9e8a;
    --ink-name: #27286a;
    --ink-text: #55565c;
    --paper: #fbfbfb;
  }
  * { box-sizing: border-box; margin: 0; padding: 0; }
  html, body {
    width: 1200px; height: 1200px; overflow: hidden;
    background: var(--backdrop);
    font-family: "Source Sans 3", "Source Sans Pro", Arial, sans-serif;
  }
  .canvas { position: relative; width: 1200px; height: 1200px; }

  .card {
    position: absolute; left: 180px; width: 840px; height: 478px;
    border-radius: 22px; overflow: hidden;
    box-shadow: 0 14px 30px rgba(0,0,0,.18);
  }
  .card--front { top: 100px; background: var(--paper); }
  .card--back {
    top: 622px;
    background: radial-gradient(circle at 40% 55%, #1d1f4c 0%, var(--navy-deep) 70%);
  }

  /* Front */
  .brand-strip {
    position: absolute; left: 0; top: 0; width: 206px; height: 100%;
    background: var(--navy);
  }
  .brand-strip__lockup {
    position: absolute; left: 50%; top: 50%;
    width: 400px; height: 120px;
    transform: translate(-50%, -50%) rotate(-90deg);
    display: flex; align-items: center; gap: 18px;
  }
  .brand-mark {
    flex: none; border-radius: 50%; background: var(--brand-blue);
  }
  .brand-strip .brand-mark { width: 30px; height: 30px; }
  .brand-strip__words { display: flex; flex-direction: column; }
  .brand-name {
    color: var(--brand-blue); font-weight: 700; line-height: 1;
  }
  .brand-strip .brand-name { font-size: 66px; }
  .tagline {
    color: var(--teal); font-weight: 700; text-transform: uppercase;
  }
  .brand-strip .tagline { font-size: 12.5px; letter-spacing: 2.6px; margin-top: 10px; }

  .contact-block { position: absolute; left: 272px; top: 88px; }
  .person-name { color: var(--ink-name); font-size: 40px; font-weight: 700; line-height: 1.05; }
  .person-role { color: var(--ink-text); font-size: 24px; line-height: 1.1; }
  .contact-list { list-style: none; margin-top: 44px; }
  .contact-item { display: flex; align-items: center; gap: 20px; margin-bottom: 16px; }
  .contact-icon {
    width: 46px; height: 46px; border-radius: 50%; background: var(--navy);
    display: flex; align-items: center; justify-content: center; flex: none;
  }
  .contact-text { color: var(--ink-text); font-size: 24px; line-height: 1.12; }

  /* Back */
  .back-lockup {
    position: absolute; left: 50%; top: 50%;
    transform: translate(-50%, -50%);
    display: flex; align-items: center; gap: 26px;
  }
  .card--back .brand-mark { width: 44px; height: 44px; }
  .card--back .brand-name { font-size: 96px; }
  .card--back .tagline { font-size: 18px; letter-spacing: 3.4px; margin-top: 8px; }
</style>
</head>
<body>
<main class="canvas">

  <section class="card card--front" aria-label="Business card front">
    <div class="brand-strip">
      <div class="brand-strip__lockup">
        <span class="brand-mark"></span>
        <div class="brand-strip__words">
          <span class="brand-name">Larkfield</span>
          <span class="tagline">Lead with lasting clarity</span>
        </div>
      </div>
    </div>

    <div class="contact-block">
      <h1 class="person-name">Daniel Hart</h1>
      <p class="person-role">Managing Director</p>
      <ul class="contact-list">
        <li class="contact-item">
          <span class="contact-icon">
            <svg width="22" height="22" viewBox="0 0 24 24" aria-hidden="true"><path fill="#2fb39a" d="M6.6 10.8a15.1 15.1 0 0 0 6.6 6.6l2.2-2.2c.3-.3.7-.4 1-.2 1.1.4 2.3.6 3.6.6.6 0 1 .4 1 1V20c0 .6-.4 1-1 1C10.6 21 3 13.4 3 4c0-.6.4-1 1-1h3.5c.6 0 1 .4 1 1 0 1.3.2 2.5.6 3.6.1.3 0 .7-.2 1z"/></svg>
          </span>
          <span class="contact-text">555.014.2286 (Cell)<br>555.014.2287 (Office)</span>
        </li>
        <li class="contact-item">
          <span class="contact-icon">
            <svg width="24" height="24" viewBox="0 0 24 24" aria-hidden="true" fill="none" stroke="#ffffff" stroke-width="1.6"><rect x="3" y="5" width="18" height="14" rx="1.5"/><line x1="3" y1="9" x2="21" y2="9"/><path d="M14 15l2 2 3-3.5" stroke="#2fb39a"/></svg>
          </span>
          <span class="contact-text">info@larkfieldconsulting.com<br>www.larkfieldconsulting.com</span>
        </li>
        <li class="contact-item">
          <span class="contact-icon">
            <svg width="24" height="24" viewBox="0 0 24 24" aria-hidden="true"><path fill="#ffffff" d="M14 3a4 4 0 0 0-4 4c0 3 4 7 4 7s4-4 4-7a4 4 0 0 0-4-4zm0 5.5A1.5 1.5 0 1 1 14 5.5a1.5 1.5 0 0 1 0 3z"/><path fill="#2fb39a" d="M4 16h8l-1 4H3z"/></svg>
          </span>
          <span class="contact-text">48 Harbor St. Suite 210<br>Fairview CA 94512</span>
        </li>
      </ul>
    </div>
  </section>

  <section class="card card--back" aria-label="Business card back">
    <div class="back-lockup">
      <span class="brand-mark"></span>
      <div>
        <div class="brand-name">Larkfield</div>
        <div class="tagline">Lead with lasting clarity</div>
      </div>
    </div>
  </section>

</main>
</body>
</html>
```